Homepage Redesign - Hi-tech business Law Firm

I'm looking for an updated graphic design (pdf file) for the homepage of dorvantlegal.ca (and which will form the general template of the other pages - but you don't need to design that). Detailed specs are in the Word file.

Deliverable is 1 pdf file that I find good looking, that sets forth the layout of the new page.

Target Market(s)

Sophisticated customers

Industry/Entity Type

Legal

Number of Pages Required

1 page

Requirements
Nice to have
• For a main background, tech type images to do with high powered boardrooms, computers, graphs, numbers, high tech manufacturing lines etc. Also, I tend to like blues and light greys, and uploaded a file today that shows my generally preferred layout, which a few of you have been getting close to.
Should not have
• Any mention of 'Personal Injury,' backgrounds that include books, or buildings with roman columns. Page should not be in dark colors or harsh on the eyes.

```html
<!DOCTYPE html>
<html lang="en">
<head>
<meta charset="utf-8">
<title>Dorvant Law Firm — Home</title>
<link href="https://fonts.googleapis.com/css2?family=Work+Sans:wght@400;500;600;700&display=swap" rel="stylesheet">
<style>
:root{
  --navy:#0e3d5f;
  --navy-dark:#0b2f4a;
  --blue:#1f5c8b;
  --link:#1a4f7a;
  --text:#222831;
  --body:#5a5f66;
  --muted:#8a9098;
  --line:#dfe3e8;
  --band:#f2f3f5;
  --white:#ffffff;
  --star:#f2a93b;
  --red:#e02b2b;
  --footer:#eef0f2;
  --bar:#1c1f24;
}
*{box-sizing:border-box;margin:0;padding:0}
html,body{width:1200px;height:3991px;overflow:hidden;background:var(--white)}
body{font-family:'Work Sans',sans-serif;color:var(--text);position:relative}
.abs{position:absolute}
.front{z-index:5}
a{color:inherit;text-decoration:none}

/* top bar */
.topbar{left:0;top:0;width:1200px;height:34px;background:var(--navy);color:var(--white);font-size:12px;display:flex;align-items:center;justify-content:center;gap:40px;z-index:5}
.topbar span{display:flex;align-items:center;gap:8px}
.topbar svg{width:13px;height:13px}

/* header */
.logo{display:flex;align-items:center;gap:8px}
.logo-box{width:50px;height:50px;border:3px solid var(--navy);background:var(--white)}
.logo-name{font-size:17px;font-weight:500;letter-spacing:3px;color:var(--navy);line-height:1.15;text-transform:uppercase}
.nav{left:390px;top:68px;width:420px;height:20px;font-size:13px;color:var(--text);z-index:5}
.nav span{position:absolute;top:0;white-space:nowrap}
.search{left:896px;top:62px;width:183px;height:31px;border:1px solid var(--line);border-radius:3px;display:flex;align-items:center;padding-left:10px;gap:8px;font-size:11px;color:#b8bdc3;background:var(--white);z-index:5}

/* hero */
.hero-visual{left:540px;top:34px;width:660px;height:588px;z-index:1;background:linear-gradient(180deg,rgba(38,52,70,0) 0%,rgba(38,52,70,0) 14%,rgba(38,52,70,0.9) 30%,#25313f 100%) 100px 0/160px 100% no-repeat,linear-gradient(110deg,#ffffff 0%,#eef5fc 30%,#8cc0ee 70%,#d6e8f8 100%)}
.hero-title{left:121px;top:214px;font-size:46px;font-weight:600;color:var(--text);z-index:5}
.hero-sub{left:121px;top:286px;font-size:30px;font-weight:400;line-height:36px;color:var(--text);z-index:5}
.btn{height:32px;border-radius:3px;font-size:11px;font-weight:600;display:flex;align-items:center;justify-content:center;gap:7px;z-index:5}
.btn-solid{left:121px;top:390px;width:112px;background:var(--navy);color:var(--white)}
.btn-line{left:246px;top:390px;width:128px;border:1.5px solid var(--navy);color:var(--navy);background:var(--white)}

/* band */
.band{left:0;top:622px;width:1200px;height:1053px;background:var(--band)}
.service{top:559px;width:306px;height:248px;background:var(--white);border:1px solid var(--line);border-radius:5px;padding:32px 26px;z-index:5}
.service svg{width:54px;height:54px;stroke:var(--navy);fill:none;stroke-width:1.6}
.service h3{font-size:20px;font-weight:400;margin-top:26px;color:var(--text)}
.service p{font-size:13px;line-height:18.5px;color:var(--body);margin-top:14px}

/* about */
.eyebrow{left:121px;top:874px;font-size:12px;font-weight:600;color:var(--navy)}
.about-title{left:121px;top:898px;font-size:30px;font-weight:400;line-height:36px;color:var(--text)}
.about-rule{left:121px;top:994px;width:220px;height:2px;background:linear-gradient(90deg,var(--navy),rgba(14,61,95,0.1))}
.about-copy{left:121px;top:1022px;width:440px;font-size:13px;line-height:18.5px;color:var(--body)}
.about-copy p{margin-bottom:18px}

/* form */
.evaluation{left:635px;top:876px;width:444px;height:466px;background:var(--white);border:1px solid var(--line);border-radius:5px}
.evaluation h3{position:absolute;left:25px;top:25px;font-size:20px;font-weight:400}
.evaluation .intro{position:absolute;left:25px;top:55px;font-size:11px;color:var(--body)}
.label{position:absolute;font-size:11px;font-weight:600;color:var(--text)}
.label b{color:var(--red);font-weight:600}
.field{position:absolute;height:32px;border:1px solid var(--line);border-radius:3px;font-size:11px;color:#c2c6cb;padding:9px 10px}
.agree{position:absolute;left:25px;top:412px;font-size:11px;line-height:16px;color:var(--body);width:300px}
.agree b{color:var(--red);font-weight:500}
.agree strong{color:var(--navy);font-weight:600}
.send{position:absolute;left:356px;top:409px;width:62px;height:32px;background:var(--navy);color:var(--white);font-size:12px;font-weight:600;border-radius:3px;display:flex;align-items:center;justify-content:center}

/* recognitions */
.round-arrow{width:38px;height:38px;border-radius:50%;background:var(--white);box-shadow:0 1px 4px rgba(0,0,0,0.12);display:flex;align-items:center;justify-content:center}
.round-arrow svg{width:16px;height:16px;stroke:var(--navy);fill:none;stroke-width:1.8}
.badge{top:1432px;height:62px;border-radius:4px}
.badge-note{top:1536px;width:330px;font-size:13px;line-height:18.5px;color:var(--body);text-align:center}

/* news */
.section-title{left:121px;font-size:30px;font-weight:400;color:var(--text)}
.news{top:1818px;width:300px;display:flex;gap:20px}
.news svg{width:26px;height:26px;flex:none;stroke:var(--navy);fill:none;stroke-width:1.3}
.news h4{font-size:13px;font-weight:600;line-height:18px;color:var(--text)}
.news p{font-size:13px;line-height:18.5px;color:var(--body);margin-top:14px;height:148px}
.news a{font-size:13px;font-weight:600;color:var(--link);display:block;margin-top:8px}
.divider{left:121px;top:2074px;width:958px;height:1px;background:var(--line)}

/* case wins */
.case-photo{top:2206px;width:390px;height:232px}
.case-text{top:2458px;width:390px}
.case-text h4{font-size:13px;font-weight:600}
.case-text p{font-size:13px;line-height:18.5px;color:var(--body);margin-top:16px}
.case-text strong{color:var(--text);font-weight:600}

/* stats */
.stats{left:121px;top:2632px;width:958px;height:148px;background:var(--band);border-radius:8px 8px 0 0;border-bottom:5px solid var(--navy)}
.stat{position:absolute;top:38px;width:200px;text-align:center}
.stat strong{display:block;font-size:44px;font-weight:400;color:var(--navy);line-height:48px}
.stat span{display:block;font-size:13px;color:var(--body);margin-top:8px}
.stat-rule{position:absolute;top:30px;width:1px;height:86px;background:var(--line)}

/* testimonials */
.review{top:2923px;width:306px;height:662px;background:var(--white);border:1px solid var(--line);border-radius:5px;padding:26px 26px}
.review .avatar{width:67px;height:67px}
.review h4{font-size:13px;font-weight:600;margin-top:26px}
.review .role{font-size:11px;color:var(--body);margin-top:5px}
.stars{display:flex;gap:5px;margin-top:10px}
.stars svg{width:14px;height:14px;fill:var(--star)}
.review p{font-size:13px;line-height:18.3px;color:var(--body);margin-top:22px;height:400px;overflow:hidden}
.review a{display:block;font-size:13px;font-weight:600;color:var(--link);margin-top:26px}

/* footer */
.footer{left:0;top:3653px;width:1200px;height:274px;background:var(--footer)}
.foot-contact{left:121px;display:flex;align-items:center;gap:10px;font-size:12px;color:var(--text)}
.foot-contact i{width:25px;height:25px;background:var(--navy);border-radius:3px;display:flex;align-items:center;justify-content:center}
.foot-contact svg{width:13px;height:13px}
.foot-about{left:435px;top:3714px;width:630px;font-size:11px;line-height:15px;color:var(--body)}
.office{top:3791px;font-size:11px;line-height:15px;color:var(--body)}
.office h5{font-size:11px;font-weight:600;color:var(--text);margin-bottom:7px}
.bottombar{left:0;top:3927px;width:1200px;height:64px;background:var(--bar);color:#c9ccd0;font-size:11px}
.bottombar .copy{position:absolute;left:121px;top:25px}
.bottombar .copy em{font-style:normal;color:#4a8fd0;margin-left:14px;padding-left:10px;border-left:1px solid #555}
.share{position:absolute;left:777px;top:20px;display:flex;align-items:center;gap:11px}
.share i{width:24px;height:24px;border-radius:50%;display:block}
</style>
</head>
<body>

<!-- hero visual (behind header) -->
<div class="abs hero-visual" role="img" aria-label="Portrait of the lead attorney in a dark suit over a soft blue network graphic"></div>

<!-- top bar -->
<div class="abs topbar">
  <span><svg viewBox="0 0 24 24" fill="none" stroke="#fff" stroke-width="2"><path d="M12 22s7-7 7-12a7 7 0 0 0-14 0c0 5 7 12 7 12z"/><circle cx="12" cy="10" r="2.5"/></svg>GTA - Hamilton - Niagara</span>
  <span><svg viewBox="0 0 24 24" fill="none" stroke="#fff" stroke-width="2"><path d="M5 3h4l2 5-2.5 1.5a11 11 0 0 0 6 6L16 13l5 2v4a2 2 0 0 1-2 2A17 17 0 0 1 3 5a2 2 0 0 1 2-2z"/></svg>555.014.2290</span>
  <span><svg viewBox="0 0 24 24" fill="none" stroke="#fff" stroke-width="2"><rect x="3" y="5" width="18" height="14" rx="1"/><path d="M3 6l9 7 9-7"/></svg>adrian@dorvantlegal.ca</span>
</div>

<!-- header -->
<div class="abs logo front" style="left:121px;top:52px">
  <div class="logo-box"></div>
  <div class="logo-name">Dorvant<br>Law Firm</div>
</div>
<nav class="abs nav">
  <span style="left:0">Practice Areas ⌄</span>
  <span style="left:133px">About ⌄</span>
  <span style="left:214px">News</span>
  <span style="left:276px">Resources</span>
  <span style="left:369px">Contact</span>
</nav>
<div class="abs search"><svg width="13" height="13" viewBox="0 0 24 24" fill="none" stroke="#0e3d5f" stroke-width="2.4"><circle cx="10.5" cy="10.5" r="6.5"/><path d="M15.5 15.5L21 21"/></svg>Search</div>

<!-- hero -->
<h1 class="abs hero-title">Winning.</h1>
<p class="abs hero-sub">My clients depend on me for it.<br>Shouldn't you?</p>
<a class="abs btn btn-solid"><svg width="13" height="13" viewBox="0 0 24 24" fill="none" stroke="#fff" stroke-width="2"><path d="M3 5h7a2 2 0 0 1 2 2v13a2 2 0 0 0-2-2H3zM21 5h-7a2 2 0 0 0-2 2v13a2 2 0 0 1 2-2h7z"/></svg>Read More</a>
<a class="abs btn btn-line"><svg width="14" height="13" viewBox="0 0 24 24" fill="none" stroke="#0e3d5f" stroke-width="2"><rect x="2" y="6" width="14" height="12" rx="1"/><path d="M16 10l6-3v10l-6-3"/></svg>Video Library</a>

<!-- grey band -->
<div class="abs band"></div>

<div class="abs service" style="left:121px">
  <svg viewBox="0 0 54 54"><rect x="3" y="6" width="20" height="44"/><rect x="23" y="20" width="16" height="30"/><rect x="39" y="32" width="12" height="18"/><path d="M8 13h4M14 13h4M8 20h4M14 20h4M8 27h4M14 27h4M8 34h4M14 34h4M28 27h6M28 34h6M43 38h4M43 44h4"/></svg>
  <h3>Business Litigation</h3>
  <p>Business disputes can have a serious impact upon your company's bottom line.</p>
</div>
<div class="abs service" style="left:447px">
  <svg viewBox="0 0 54 54"><rect x="3" y="18" width="48" height="32" rx="3"/><path d="M19 18v-6h16v6M3 30h48M22 26h10v8H22z"/><path d="M34 10V3h10v11"/></svg>
  <h3>Professional Negligence</h3>
  <p>When a professional has let you down, the impact can be devastating. I have the experience need to help.</p>
</div>
<div class="abs service" style="left:774px">
  <svg viewBox="0 0 54 54"><path d="M10 20a14 14 0 0 1 28 0zM24 20v14"/><path d="M4 40l8-4h10l6 3h-8M20 41h10l14-8c3-1 5 2 3 4l-15 10H12l-8 2"/></svg>
  <h3>Insurance</h3>
  <p>When your insurance company refuses to pay, you need a lawyer who has experience suing insurance companies, and winning</p>
</div>

<!-- about -->
<div class="abs eyebrow">Your Experienced Toronto and Hamilton Lawyers</div>
<h2 class="abs about-title">Getting the Results That<br>Matter</h2>
<div class="abs about-rule"></div>
<div class="abs about-copy">
  <p>Dorvant Law Firm is a boutique litigation firm with law offices in Toronto and Hamilton. We concentrate our legal practice on complex business litigation, professional negligence (malpractice) claims, commercial contract disputes, and insurance coverage disputes.</p>
  <p>We take an innovative approach to our client's legal problems, and are guided by the philosophy that our job is to get results.</p>
  <p>The lawyers at Dorvant Law Firm have the reputation for vigorously representing their clients' interests and competing hard to obtain the best possible results. With experience at all stages of legal disputes, the lawyers at Dorvant Law Firm are equally at home negotiating in a boardroom or presenting a case at trial.</p>
  <p>We hope that you take the time to explore our website to find out how our record of excellence, expertise and many years of experience can assist you.</p>
</div>

<!-- case evaluation form -->
<form class="abs evaluation">
  <h3>Case Evaluation</h3>
  <p class="intro">Fill out this form to schedule your initial consult with our lawyers.</p>
  <span class="label" style="left:25px;top:91px">Name <b>*</b></span>
  <div class="field" style="left:25px;top:110px;width:191px">First Name</div>
  <div class="field" style="left:227px;top:110px;width:191px">Last Name</div>
  <span class="label" style="left:25px;top:163px">Email <b>*</b></span>
  <span class="label" style="left:227px;top:163px">Phone <b>*</b></span>
  <div class="field" style="left:25px;top:182px;width:191px">Email Address</div>
  <div class="field" style="left:227px;top:182px;width:191px">Phone Number</div>
  <span class="label" style="left:25px;top:235px">Case Details <b>*</b></span>
  <div class="field" style="left:25px;top:254px;width:393px;height:132px">Case Details</div>
  <p class="agree"><b>*</b>&nbsp; By using this site and/or submitting this form, I<br>&nbsp;&nbsp;&nbsp;agree to the <strong>Privacy Policy</strong> and <strong>Terms of Use</strong>.</p>
  <div class="send">Send</div>
</form>

<!-- recognitions -->
<div class="abs round-arrow" style="left:121px;top:1444px"><svg viewBox="0 0 24 24"><path d="M20 12H4M10 6l-6 6 6 6"/></svg></div>
<div class="abs round-arrow" style="left:1041px;top:1444px"><svg viewBox="0 0 24 24"><path d="M4 12h16M14 6l6 6-6 6"/></svg></div>
<div class="abs badge" style="left:293px;width:208px;background:var(--red)" role="img" aria-label="Peer rating recognition badge"></div>
<div class="abs badge" style="left:690px;width:228px;background:linear-gradient(90deg,#e9c23c 0 40px,#d9dce0 40px)" role="img" aria-label="Provincial law society membership badge"></div>
<p class="abs badge-note" style="left:232px">An excellent rating for a lawyer with some experience. This rating indicates the attorney is widely respected by their peers for high professional achievement and ethical standards.</p>
<p class="abs badge-note" style="left:639px">An excellent rating for a lawyer with some experience. This rating indicates the attorney is widely respected by their peers for high professional achievement and ethical standards.</p>

<!-- news -->
<h2 class="abs section-title" style="top:1742px">Latest News</h2>
<article class="abs news" style="left:121px">
  <svg viewBox="0 0 26 26"><rect x="1" y="3" width="24" height="20" rx="2"/><path d="M5 8h7v6H5zM15 8h6M15 11h6M15 14h6M5 18h16"/></svg>
  <div><h4>Dorvant Law Firm joins Global Referral Network</h4>
  <p>Dorvant Law Firm, is now a member of Meridian Global Referral Network — the largest legal referral network in the world — comprising 283 member firms located in more than 160 countries.</p>
  <a>Read More</a></div>
</article>
<article class="abs news" style="left:452px">
  <svg viewBox="0 0 26 26"><rect x="1" y="3" width="24" height="20" rx="2"/><path d="M5 8h7v6H5zM15 8h6M15 11h6M15 14h6M5 18h16"/></svg>
  <div><h4>How to Get the Most out of an Initial Consultation with a Lawyer</h4>
  <p>If you're contemplating legal action, have been sued, are unsure of your legal standing in a particular situation, or need advice on an issue that has potential legal ramifications, your first port of call should be to seek proper…</p>
  <a>Read More</a></div>
</article>
<article class="abs news" style="left:783px">
  <svg viewBox="0 0 26 26"><rect x="1" y="3" width="24" height="20" rx="2"/><path d="M5 8h7v6H5zM15 8h6M15 11h6M15 14h6M5 18h16"/></svg>
  <div><h4>How to Protect Yourself During Construction/Renovations</h4>
  <p>Construction and renovation expenses can be substantial, often in excess of $100,000.00. While many projects go smoothly, others do not. Contractors (or subcontractors) can fail to build to specification, damage…</p>
  <a>Read More</a></div>
</article>
<div class="abs divider"></div>

<!-- case wins -->
<h2 class="abs section-title" style="top:2131px">Case Wins</h2>
<div class="abs round-arrow" style="left:121px;top:2320px"><svg viewBox="0 0 24 24"><path d="M20 12H4M10 6l-6 6 6 6"/></svg></div>
<div class="abs round-arrow" style="left:1041px;top:2320px"><svg viewBox="0 0 24 24"><path d="M4 12h16M14 6l6 6-6 6"/></svg></div>
<div class="abs case-photo" style="left:193px;background:linear-gradient(180deg,#b9c3c9 0%,#c7b79a 30%,#d8742f 55%,#8a8377 75%,#6f6a62 100%)" role="img" aria-label="Row of impounded orange and white buses in a lot"></div>
<div class="abs case-photo" style="left:616px;background:linear-gradient(180deg,#dfe2e5 0%,#cfd3d7 45%,#6d6860 62%,#eceeef 78%,#f6f7f8 100%)" role="img" aria-label="Lawyer signing documents at a desk beside scales of justice"></div>
<div class="abs case-text" style="left:193px">
  <h4>Injunction</h4>
  <p>Secured a Court Order appointing a Receiver and directing the Sheriff to seize all assets of a transportation company, resulting in approximately 20 buses and shuttles being pulled off the road and impounded.</p>
</div>
<div class="abs case-text" style="left:616px">
  <h4>Summary – Judgment</h4>
  <p>Defeated Defendant's motion for summary judgment on a <strong>multi-million dollar</strong> claim involving a minor who suffered severe brain injuries.</p>
</div>

<!-- stats -->
<div class="abs stats">
  <div class="stat" style="left:76px"><strong>17+</strong><span>Years of Litigation</span></div>
  <div class="stat-rule" style="left:278px"></div>
  <div class="stat" style="left:277px"><strong>234</strong><span>Cases Won</span></div>
  <div class="stat-rule" style="left:478px"></div>
  <div class="stat" style="left:479px"><strong>15</strong><span>Awards</span></div>
  <div class="stat-rule" style="left:679px"></div>
  <div class="stat" style="left:680px"><strong>5.0</strong><span>Customers Rating</span></div>
</div>

<!-- testimonials -->
<h2 class="abs section-title" style="top:2847px">What Our Clients Are Saying</h2>
<article class="abs review" style="left:121px">
  <div class="avatar" style="background:linear-gradient(135deg,#6b4e3d,#c9a48a)" role="img" aria-label="Client photo"></div>
  <h4>Nora Whitfield</h4>
  <div class="role">Litigation Client</div>
  <div class="stars"><svg viewBox="0 0 24 24"><path d="M12 2l3 7h7l-5.5 4.5 2 7.5-6.5-4.5-6.5 4.5 2-7.5L2 9h7z"/></svg><svg viewBox="0 0 24 24"><path d="M12 2l3 7h7l-5.5 4.5 2 7.5-6.5-4.5-6.5 4.5 2-7.5L2 9h7z"/></svg><svg viewBox="0 0 24 24"><path d="M12 2l3 7h7l-5.5 4.5 2 7.5-6.5-4.5-6.5 4.5 2-7.5L2 9h7z"/></svg><svg viewBox="0 0 24 24"><path d="M12 2l3 7h7l-5.5 4.5 2 7.5-6.5-4.5-6.5 4.5 2-7.5L2 9h7z"/></svg><svg viewBox="0 0 24 24"><path d="M12 2l3 7h7l-5.5 4.5 2 7.5-6.5-4.5-6.5 4.5 2-7.5L2 9h7z"/></svg></div>
  <p>I cannot say enough about having Adrian Dorvant as my lawyer! I found him during a very difficult and stressful time and was so nervous about finding a good lawyer after having a few bad experiences. The experience that I had with Adrian eased ALL of that anxiety for me! He worked very very hard on my settlement and was very reassuring and truly cared about my situation. I always knew what was going on with my case as he always kept me updated with phone calls, emails and everything that was pertained to my case... I highly recommend Adrian Dorvant as a lawyer and if you would like someone who is thorough and who truly cares about your case and you as a person than this is the man to go to!!!</p>
  <a>Read More</a>
</article>
<article class="abs review" style="left:447px">
  <div class="avatar" style="background:linear-gradient(135deg,#3a3430,#b79b86)" role="img" aria-label="Client photo"></div>
  <h4>Paul &amp; Dana Merrick</h4>
  <div class="role">Business Litigation Clients</div>
  <div class="stars"><svg viewBox="0 0 24 24"><path d="M12 2l3 7h7l-5.5 4.5 2 7.5-6.5-4.5-6.5 4.5 2-7.5L2 9h7z"/></svg><svg viewBox="0 0 24 24"><path d="M12 2l3 7h7l-5.5 4.5 2 7.5-6.5-4.5-6.5 4.5 2-7.5L2 9h7z"/></svg><svg viewBox="0 0 24 24"><path d="M12 2l3 7h7l-5.5 4.5 2 7.5-6.5-4.5-6.5 4.5 2-7.5L2 9h7z"/></svg><svg viewBox="0 0 24 24"><path d="M12 2l3 7h7l-5.5 4.5 2 7.5-6.5-4.5-6.5 4.5 2-7.5L2 9h7z"/></svg><svg viewBox="0 0 24 24"><path d="M12 2l3 7h7l-5.5 4.5 2 7.5-6.5-4.5-6.5 4.5 2-7.5L2 9h7z"/></svg></div>
  <p>We highly recommend Adrian Dorvant, he truly comes as advertised. My Wife and I were caught in a long drawn out civil action over an asset purchase agreement that lasted almost 5 years. We had previously changed lawyers 3 times and were in a dire situation less than 2 months from trial. We needed someone who cared about their clients, was ethical, knowledgeable, dedicated, and affordable. After endless searching we found Dorvant Law Firm, contacted him, and were amazed by his dedication to our file. He was well informed within a few weeks and did more work in 6 weeks than the other firms did over 5 years. He contacted all witnesses, studied the transcripts, documents, talked with us constantly, and made excellent use of all resources availab...</p>
  <a>Read More</a>
</article>
<article class="abs review" style="left:774px">
  <div class="avatar" style="background:linear-gradient(135deg,#4a4e55,#c8c3bd)" role="img" aria-label="Client photo"></div>
  <h4>Victor (Vic) Alvarado</h4>
  <div class="role">Owner-LREB Coastline Home Realty</div>
  <div class="stars"><svg viewBox="0 0 24 24"><path d="M12 2l3 7h7l-5.5 4.5 2 7.5-6.5-4.5-6.5 4.5 2-7.5L2 9h7z"/></svg><svg viewBox="0 0 24 24"><path d="M12 2l3 7h7l-5.5 4.5 2 7.5-6.5-4.5-6.5 4.5 2-7.5L2 9h7z"/></svg><svg viewBox="0 0 24 24"><path d="M12 2l3 7h7l-5.5 4.5 2 7.5-6.5-4.5-6.5 4.5 2-7.5L2 9h7z"/></svg><svg viewBox="0 0 24 24"><path d="M12 2l3 7h7l-5.5 4.5 2 7.5-6.5-4.5-6.5 4.5 2-7.5L2 9h7z"/></svg><svg viewBox="0 0 24 24"><path d="M12 2l3 7h7l-5.5 4.5 2 7.5-6.5-4.5-6.5 4.5 2-7.5L2 9h7z"/></svg></div>
  <p>As a real estate broker we encountered a transaction where we needed the expertise of a litigation attorney to help us collect a disputed commission. The transaction was very complicated and we needed an attorney that would be extremely thorough. After interviewing several attorney's we settled on Adrian Dorvant, ESQ., as our legal representative. To our good fortune it was the best decision we made. In short order, Adrian prepared a plan and worked tirelessly, including many late evenings interviewing us, reviewing the documents, case history, and real estate law. During our second final hearing Adrian prepared the most skillful, articulate case defense that the hearing judge awarded us an acceptable settlemen...</p>
  <a>Read More</a>
</article>

<!-- footer -->
<footer class="abs footer"></footer>
<div class="abs logo" style="left:121px;top:3706px">
  <div class="logo-box"></div>
  <div class="logo-name">Dorvant<br>Law Firm</div>
</div>
<div class="abs foot-contact" style="top:3778px"><i><svg viewBox="0 0 24 24" fill="none" stroke="#fff" stroke-width="2"><path d="M12 22s7-7 7-12a7 7 0 0 0-14 0c0 5 7 12 7 12z"/><circle cx="12" cy="10" r="2.5"/></svg></i>GTA - Hamilton - Niagara</div>
<div class="abs foot-contact" style="top:3813px;color:var(--link)"><i><svg viewBox="0 0 24 24" fill="none" stroke="#fff" stroke-width="2"><path d="M5 3h4l2 5-2.5 1.5a11 11 0 0 0 6 6L16 13l5 2v4a2 2 0 0 1-2 2A17 17 0 0 1 3 5a2 2 0 0 1 2-2z"/></svg></i>555.014.2290</div>
<div class="abs foot-contact" style="top:3848px;color:var(--link)"><i><svg viewBox="0 0 24 24" fill="none" stroke="#fff" stroke-width="2"><rect x="3" y="5" width="18" height="14" rx="1"/><path d="M3 6l9 7 9-7"/></svg></i>adrian@dorvantlegal.ca</div>
<p class="abs foot-about">Dorvant Law Firm is a boutique law office concentrating in Complex Business Litigation, Professional Negligence, Commercial Disputes, and Insurance Coverage Disputes. Our innovative and pugnacious approach gets results for our clients in the Greater Toronto Area. HST #100200300RT00001</p>
<div class="abs office" style="left:435px"><h5>Hamilton Office</h5>14 Harbour Lane E,<br>Ground Floor Hamilton,<br>ON L8N 0A1</div>
<div class="abs office" style="left:627px"><h5>Toronto Office</h5>220 Bay Crest Road #3100,<br>Toronto,<br>ON M5X 0B2</div>
<div class="abs office" style="left:828px"><h5>Niagara Office</h5>8 Orchard Row,<br>Virgil,<br>ON L0S 0A3</div>

<div class="abs bottombar">
  <div class="copy">© 2023 Dorvant Law Firm. All Rights Reserved.<em>Sitemap</em></div>
  <div class="share">Share this page:
    <i style="background:#1f6fd8"></i>
    <i style="background:#c8357f"></i>
    <i style="background:#2fb24c"></i>
    <i style="background:#2b9de8"></i>
    <i style="background:#1366b0"></i>
    <i style="background:#d0232c"></i>
  </div>
</div>

</body>
</html>
```